Save Us! Grand Opening Rescue + Outreach Center Flyers for our Animals

Flyers to describe the different areas and animals in our new rescue + outreach center. We are a charity that rescues animals from animal testing and other forms of abuse. We have a grand opening next month and need great descriptive flyers in order to educate people and raise funds.
Updates

I need to provide more information for the designers.

Target Market(s)

Those interested in donating, volunteering and helping us save animals.

Industry/Entity Type

Non-Profit

Font styles to use
Sans Serif

Colors

Designer to choose colors to be used in the design.

Requirements
Must have
• Colors and photos. Feel free to edit the Dusty photos to make them fit in the flyer, use 1 or both, whatever you like.
• Here is the text for the main flyer, although there are a few flyers, but they can be interchangeable:
• Senior & Special Needs Dogs
• At the TEL, these dogs will have their very own retreat and retirement center to experience the best in care & relaxation!
• Survivor Spotlight: Dusty
• Dusty was rescued by KHW after being abandoned. His lower body was completely paralyzed, unable to use his hind legs. After nearly 1 year of rehabilitation, KHW found him his forever family and Dusty is in a specialized wheelchair so he can run and play with his forever family, and be the puppy he is!
• Help us enrich the lives of our senior & special needs dogs by donating today and save more survivors, just like Dusty!
• Questions about donating to the TEL? Please contact our President at gretchen@khwrescue.org
Nice to have
• Playful.
Should not have
• No sharp edges, not too serious, yet has a point - asking for donations and educational aspect must come across.

```html
<!DOCTYPE html>
<html lang="en">
<head>
<meta charset="utf-8">
<title>Senior &amp; Special Needs Dogs at the TEL – Survivor Spotlight: Dusty</title>
<link href="https://fonts.googleapis.com/css2?family=Fredoka:wght@500;600&family=Lilita+One&family=Open+Sans:ital,wght@1,700&display=swap" rel="stylesheet">
<style>
  :root {
    --pink: #e8768a;
    --pink-light: #f08ea0;
    --pink-deep: #de6a7f;
    --cream: #f4d8b8;
    --cream-pale: #fbeede;
    --teal: #2f6a6a;
    --logo-pink: #e07283;
    --white: #ffffff;
    --ink-shadow: rgba(120, 40, 55, 0.45);
  }
  * { margin: 0; padding: 0; box-sizing: border-box; }
  html, body { width: 839px; height: 1200px; overflow: hidden; background: var(--white); }
  .flyer { position: relative; width: 839px; height: 1200px; overflow: hidden; font-family: "Fredoka", sans-serif; }

  .hero { position: absolute; left: 0; top: 0; width: 839px; height: 367px; overflow: hidden; }
  .hero-photo { position: absolute; inset: 0; }
  .brand { position: absolute; left: 48px; top: 158px; display: flex; align-items: center; gap: 14px; }
  .brand-circle { width: 54px; height: 54px; border-radius: 50%; border: 3px solid var(--logo-pink); }
  .brand-name { font-weight: 600; font-size: 50px; line-height: 1; color: var(--logo-pink); letter-spacing: 2px; }
  .hero-title { position: absolute; right: 30px; top: 324px; font-weight: 600; font-size: 28px; line-height: 34px; color: var(--teal); letter-spacing: 0.8px; white-space: nowrap; }

  .feature { position: absolute; left: 0; top: 367px; width: 839px; height: 772px;
    background: radial-gradient(ellipse at 50% 40%, var(--pink-light) 0%, var(--pink) 55%, var(--pink-deep) 100%); }
  .intro, .appeal { position: absolute; left: 0; width: 839px; text-align: center; font-weight: 500; font-size: 25px; line-height: 28px; color: var(--cream); letter-spacing: 1.1px; white-space: nowrap; text-shadow: 0 1px 3px var(--ink-shadow); }
  .intro { top: 18px; }
  .appeal { top: 705px; }
  .spotlight-title { position: absolute; left: 0; top: 100px; width: 839px; text-align: center; font-family: "Lilita One", sans-serif; font-weight: 400; font-size: 62px; line-height: 1; letter-spacing: 3px; color: var(--cream); text-transform: uppercase; text-shadow: 0 3px 6px var(--ink-shadow); }

  .portrait-frame { position: absolute; left: 23px; top: 172px; width: 526px; height: 526px; border-radius: 50%; background: var(--cream); padding: 10px; }
  .portrait { display: block; width: 100%; height: 100%; border-radius: 50%; }

  .survivor-name { position: absolute; left: 432px; top: 172px; font-family: "Lilita One", sans-serif; font-size: 124px; line-height: 1; letter-spacing: 2px; color: var(--cream); transform: rotate(-4deg); transform-origin: left bottom; text-shadow: 0 4px 8px var(--ink-shadow); }

  .paw { position: absolute; }

  .story { position: absolute; right: 38px; top: 384px; text-align: right; white-space: nowrap; font-family: "Open Sans", sans-serif; font-style: italic; font-weight: 700; font-size: 22px; line-height: 26.6px; color: var(--cream-pale); text-shadow: 0 2px 3px var(--ink-shadow); }

  .contact { position: absolute; left: 0; top: 1155px; width: 839px; text-align: center; white-space: nowrap; font-weight: 600; font-size: 17.5px; line-height: 24px; color: var(--teal); }
</style>
</head>
<body>
<main class="flyer">
  <header class="hero">
    <svg class="hero-photo" width="839" height="367" role="img" aria-label="Photo of a white and ginger cat snuggled against a resting golden retriever on a cream shag rug">
      <defs>
        <linearGradient id="heroBg" x1="0" y1="0" x2="1" y2="0">
          <stop offset="0" stop-color="#efe4dc"/>
          <stop offset="0.3" stop-color="#f1dccb"/>
          <stop offset="0.5" stop-color="#fbf5f0"/>
          <stop offset="0.62" stop-color="#f3d6b6"/>
          <stop offset="0.78" stop-color="#dc9e5c"/>
          <stop offset="0.9" stop-color="#c98a4c"/>
          <stop offset="1" stop-color="#efe6dc"/>
        </linearGradient>
        <linearGradient id="rug" x1="0" y1="0" x2="0" y2="1">
          <stop offset="0" stop-color="#f8f2e8" stop-opacity="0"/>
          <stop offset="1" stop-color="#f8f2e8" stop-opacity="0.95"/>
        </linearGradient>
      </defs>
      <rect width="839" height="367" fill="url(#heroBg)"/>
      <rect y="240" width="839" height="127" fill="url(#rug)"/>
    </svg>
    <div class="brand">
      <span class="brand-circle"></span>
      <span class="brand-name">THE TEL</span>
    </div>
    <h1 class="hero-title">Senior &amp; Special Needs Dogs At the TEL,</h1>
  </header>

  <section class="feature">
    <p class="intro">These dogs will have their very own retreat and<br>retirement center to experience the best in care &amp; relaxation!</p>
    <h2 class="spotlight-title">Survivor Spotlight:</h2>

    <div class="portrait-frame">
      <svg class="portrait" viewBox="0 0 506 506" role="img" aria-label="Photo of Dusty, a young black Labrador in an orange bandana, standing on grass in his wheelchair">
        <defs>
          <radialGradient id="portraitBg" cx="0.5" cy="0.55" r="0.6">
            <stop offset="0" stop-color="#2a2a2a"/>
            <stop offset="0.55" stop-color="#3d4a2a"/>
            <stop offset="1" stop-color="#5e8a3a"/>
          </radialGradient>
        </defs>
        <circle cx="253" cy="253" r="253" fill="url(#portraitBg)"/>
      </svg>
    </div>

    <div class="survivor-name">DUSTY</div>

    <svg class="paw" style="left:38px;top:187px" width="52" height="58" role="img" aria-label="Paw print decoration"><ellipse cx="26" cy="34" rx="24" ry="22" fill="var(--cream)"/></svg>
    <svg class="paw" style="left:608px;top:285px" width="80" height="92" role="img" aria-label="Paw print decoration"><ellipse cx="40" cy="52" rx="38" ry="36" fill="var(--cream)"/></svg>
    <svg class="paw" style="left:46px;top:637px" width="54" height="62" role="img" aria-label="Paw print decoration"><ellipse cx="27" cy="35" rx="25" ry="24" fill="var(--cream)"/></svg>

    <p class="story">Dusty was rescued by KHW<br>after being abandoned.<br>His lower body was<br>completely paralyzed,<br>unable to use his hind legs.<br>After nearly 1 year of rehabilitation,<br>KHW found him his forever family<br>and Dusty is in a specialized<br>wheelchair so he can run and<br>play with his forever family,<br>and be the puppy he is!</p>

    <p class="appeal">Help us enrich the lives of our senior &amp; special needs dogs by<br>donating today and save more survivors, just like Dusty!</p>
  </section>

  <footer class="contact">Questions about donating to the TEL? Please contact our President at gretchen@khwrescue.org</footer>
</main>
</body>
</html>
```